Ridgeback Petroleum Ventures, LLC

Our website (www.ridgebackpetroventures.example) is poorly done and dated. I want to redo it with one main page and wide format photos or oil & gas drilling and production. Perhaps all of the pages listed on the left side of the existing site could be viewed by scrolling down further on the new main page. I want something clean and easy to navigate.

Target Market(s)

Other oil and gas companies and people that we have contacted regarding selling or leasing their mineral rights. These people will come to our website to research our company and become more comfortable doing business with us.

Industry/Entity Type

Oil And Gas

Coding

Coded - Design and coding required

Number of Pages Required

1 page

Font styles to use
Serif

Requirements
Must have
• Clean and uncluttered. Nice, clear wide format picture or oil well or rig and landscape.

```html
<!DOCTYPE html>
<html lang="en">
<head>
<meta charset="utf-8">
<title>Ridgeback Petroleum Ventures, LLC</title>
<link href="https://fonts.googleapis.com/css2?family=Alegreya:wght@400;700&family=Open+Sans:wght@400;600;700&display=swap" rel="stylesheet">
<style>
:root{
  --orange:#f07a1e;
  --orange-dark:#c9631a;
  --rust:#b9571c;
  --ink:#333;
  --muted:#555;
  --dark:#1f1f1f;
  --darker:#141414;
  --white:#fff;
  --serif:'Alegreya', Georgia, serif;
  --sans:'Open Sans', Arial, sans-serif;
}
*{box-sizing:border-box;margin:0;padding:0}
html,body{width:1200px;height:3468px;overflow:hidden}
body{font-family:var(--sans);color:var(--ink);background:#fff;position:relative;font-size:14px}
section,header,footer{position:absolute;left:0;width:1200px}
.wrap{position:absolute;left:81px;width:1040px}
.h2{font-family:var(--serif);font-size:38px;color:var(--orange);display:flex;align-items:center;gap:8px;font-weight:400}
.h2 .mark{width:10px;height:28px;background:currentColor;opacity:.55;border-radius:2px}
p.lede{font-size:13.5px;line-height:1.65;color:var(--muted)}
.photo{position:absolute}

/* hero */
.hero{top:0;height:578px;background:linear-gradient(110deg,#5a5e63 0%,#3b3f44 40%,#6b5a4a 70%,#2c3036 100%)}
.topbar{position:absolute;top:0;right:81px;height:32px;display:flex;gap:30px;align-items:center;color:#eee;font-size:13px}
.topbar span{display:flex;gap:7px;align-items:center}
.nav{position:absolute;top:42px;left:81px;width:1040px;height:78px;background:#fff;display:flex;align-items:center;justify-content:space-between;padding:0 26px}
.brand{display:flex;align-items:center;gap:10px}
.brand .dot{width:30px;height:30px;border-radius:50%;background:var(--orange)}
.brand b{font-family:var(--serif);font-size:30px;color:#222;display:block;line-height:1}
.brand small{font-size:10px;color:#222;display:block}
.menu{display:flex;gap:30px;align-items:center;font-size:13.5px}
.menu .cta{background:var(--orange);color:#fff;padding:10px 16px}
.hero h1{position:absolute;left:81px;top:238px;font-family:var(--serif);font-weight:400;font-size:46px;color:#fff}
.hero p{position:absolute;left:81px;top:300px;width:560px;color:#fff;font-size:13.5px;line-height:1.6}
.btn{display:inline-block;background:var(--orange);color:#fff;font-weight:700;font-size:14px}
.hero .btn{position:absolute;left:81px;top:381px;height:44px;line-height:44px;padding:0 24px}
.arrows{position:absolute;right:81px;top:520px;color:#fff;font-size:26px;display:flex;gap:22px}

/* history */
.history{top:578px;height:421px}
.history .h2{position:absolute;left:81px;top:52px}
.history .txt{position:absolute;left:81px;top:110px;width:540px}
.history .txt p{margin-bottom:20px;font-size:13px;line-height:1.7}
.history .photo{left:652px;top:46px;width:474px;height:319px;background:linear-gradient(180deg,#8ab7d8 0%,#4f86ad 55%,#2f5f80 100%);box-shadow:6px 6px 0 #ddd}

/* about */
.about{top:999px;height:661px;background:linear-gradient(120deg,var(--orange) 0%,#e56f16 100%);color:#fff}
.about .h2{color:#fff;position:absolute;left:81px;top:42px}
.about .intro{position:absolute;left:81px;top:100px;width:650px;font-size:13px;line-height:1.65}
.ticks{position:absolute;left:81px;top:175px;width:650px;display:grid;grid-template-columns:1fr 1fr;row-gap:12px;font-size:13px}
.ticks span{display:flex;gap:10px;align-items:center}
.video{left:81px;top:259px;width:647px;height:349px;background:linear-gradient(160deg,#6d6a4e,#3e4a4c 60%,#2a2f33)}
.play{position:absolute;left:50%;top:50%;transform:translate(-50%,-62%);text-align:center;color:#fff;font-size:18px;letter-spacing:1px}
.play .ring{width:84px;height:84px;border-radius:50%;background:var(--orange);margin:0 auto 14px;display:flex;align-items:center;justify-content:center}
.members-title{position:absolute;left:761px;top:46px;font-size:19px;font-weight:600}
.member{position:absolute;left:761px;width:360px;height:155px;background:#fff;color:var(--muted);padding:18px 18px}
.member .who{display:flex;align-items:center;gap:12px;font-family:var(--serif);font-weight:700;font-size:17px;color:#333;border-bottom:1px solid #eee;padding-bottom:12px}
.member .who i{width:40px;height:40px;border-radius:50%;border:2px solid #ccc;background:#eee}
.member p{font-size:12px;line-height:1.6;margin-top:12px}
.member a{color:var(--orange);font-size:12px;font-weight:600;text-decoration:none}

/* prospects */
.prospects{top:1660px;height:467px}
.prospects .h2{position:absolute;left:81px;top:50px}
.prospects p.lede{position:absolute;left:81px;top:106px;width:1040px}
.card{position:absolute;top:183px;width:312px;height:231px}
.card .img{height:190px}
.card .cap{height:41px;background:var(--orange);color:#fff;text-align:center;line-height:41px;font-size:12.5px;letter-spacing:.5px}

/* contact */
.contact{top:2127px;height:432px;background:var(--dark);color:#fff}
.contact .h2{color:#fff;position:absolute;left:81px;top:50px}
.contact p.lede{position:absolute;left:81px;top:108px;width:1040px;color:#ddd}
.addr{position:absolute;top:171px;width:235px;height:206px;background:#fff;color:var(--muted);padding:18px 18px;font-size:12px;line-height:1.75}
.addr h4{display:flex;gap:8px;align-items:center;font-size:13px;color:#333;font-weight:600;margin-bottom:6px}
.addr.hi{background:var(--orange);color:#fff}.addr.hi h4{color:#fff}
.addr .ln{display:flex;gap:8px;align-items:center}

/* enquiry */
.enquiry{top:2559px;height:255px;background:var(--rust)}
.enquiry h3{position:absolute;top:50px;width:100%;text-align:center;font-family:var(--serif);font-weight:400;font-size:23px;color:#fff;letter-spacing:1px}
.field{position:absolute;height:38px;border:1px solid rgba(255,255,255,.3);color:#fff;font-size:12px;padding:10px 10px}
.enquiry .btn{position:absolute;left:867px;top:107px;width:254px;height:79px;line-height:79px;text-align:center;background:#fff;color:var(--orange);font-size:17px}

/* clients */
.clients{top:2814px;height:273px}
.clients .h2{position:absolute;left:81px;top:50px}
.clients p.lede{position:absolute;left:81px;top:106px;width:1040px}
.logos{position:absolute;left:81px;top:168px;width:1040px;height:66px;display:flex;align-items:center}
.logos span{flex:1;text-align:center;font-family:var(--sans);font-weight:700;font-size:19px;color:#444;border-left:1px solid #ddd}
.logos span:first-child{border-left:0}

/* footer */
.footer{top:3087px;height:330px;background:var(--darker);color:#ddd}
.footer .brand{position:absolute;left:81px;top:50px}
.footer .brand b,.footer .brand small{color:#fff}
.footer .about-txt{position:absolute;left:81px;top:120px;width:330px;font-size:12.5px;line-height:1.7}
.social{position:absolute;left:81px;top:235px;display:flex;height:36px;background:var(--orange);padding:0 8px;gap:8px;align-items:center}
.social i{width:14px;height:14px;background:#fff;opacity:.85}
.phone-btn{position:absolute;left:206px;top:235px;height:36px;width:160px;background:var(--orange);color:#fff;display:flex;align-items:center;justify-content:center;gap:8px;font-size:14px}
.col{position:absolute;top:50px}
.col h5{font-size:13px;font-weight:600;letter-spacing:1px;color:#fff;margin-bottom:24px}
.col li{list-style:none;font-size:12px;line-height:20px}
.quote{font-size:12px;line-height:1.65;margin-bottom:16px;width:260px}
.quote b{color:#fff;font-style:italic;display:flex;gap:10px;margin-bottom:4px}
.news{display:flex;margin-top:14px}
.news span{width:126px;height:40px;background:#2a2a2a;font-size:11.5px;padding:12px 10px}
.news i{width:44px;height:40px;background:var(--orange);display:flex;align-items:center;justify-content:center}
.bottom{top:3417px;height:51px;background:#0c0c0c;color:#ccc;font-size:12px}
.bottom span{position:absolute;top:18px}
</style>
</head>
<body>

<header class="hero">
  <div class="photo" style="inset:0;background:inherit" role="img" aria-label="Wide photo of engineers in hard hats working among refinery pipework"></div>
  <div class="topbar">
    <span><svg width="12" height="12" viewBox="0 0 24 24"><path fill="#fff" d="M6.6 10.8a15 15 0 0 0 6.6 6.6l2.2-2.2a1 1 0 0 1 1-.25 11 11 0 0 0 3.6.6 1 1 0 0 1 1 1V20a1 1 0 0 1-1 1A17 17 0 0 1 3 4a1 1 0 0 1 1-1h3.5a1 1 0 0 1 1 1 11 11 0 0 0 .6 3.6 1 1 0 0 1-.25 1z"/></svg>555.010.2400</span>
    <span><svg width="14" height="11" viewBox="0 0 14 11"><rect x=".5" y=".5" width="13" height="10" fill="none" stroke="#fff"/><path d="M.5.5 7 6l6.5-5.5" fill="none" stroke="#fff"/></svg>inquiry@ridgebackpetroventures.example</span>
  </div>
  <nav class="nav">
    <div class="brand"><span class="dot"></span><div><b>Ridgeback</b><small>Petroleum Ventures, LLC</small></div></div>
    <div class="menu"><span>Home</span><span>History</span><span>About Us</span><span>Available Prospects</span><span>Texas</span><span>Oklahoma</span><span class="cta">Contact Us</span></div>
  </nav>
  <h1>World-Class Gas &amp; Oil Servies</h1>
  <p>Sed ut perspiciatis unde omnis iste natus error sit voluptatem accusantium doloremque laudantium, totam rem aperiam, eaque ipsa quae ab illo inventore veritatis et quasi architecto beatae vitae dicta sunt explicabo.</p>
  <span class="btn">GET FREE QUOTE</span>
  <div class="arrows"><span>&#8249;</span><span>&#8250;</span></div>
</header>

<section class="history">
  <h2 class="h2"><span class="mark"></span>History</h2>
  <div class="txt">
    <p>Ridgeback Petroleum Ventures, LLC was founded in 2011 by Alden Marsh. In 2012 Dale Marsh &amp; Curtis Marsh joined the company. In 2013, Wade Ellison joined the company as a Petroleum Engineer and in 2015, became a partner. Ridgeback has expanded their business, and currently has offices located in Fort Worth and Oklahoma City.</p>
    <p>Since 2012 Ridgeback has acquired more than 25,000 net acres of leasehold in Texas, Oklahoma and Kansas. During the same time, the company has also purchased in excess of 10,000 mineral acres primarily in Oklahoma and to a lesser extent, East Texas. In addition, Ridgeback has participated in hundreds of wells with top tier operators.</p>
  </div>
  <div class="photo" role="img" aria-label="Offshore drilling platform on the water with a supply boat"></div>
</section>

<section class="about">
  <h2 class="h2"><span class="mark"></span>About Us</h2>
  <p class="intro">Sed ut perspiciatis unde omnis iste natus error sit voluptatem accusantium doloremque laudantium, totam rem aperiam, eaque ipsa quae ab illo inventore veritatis et quasi architecto beatae vitae dicta sunt explicabo.</p>
  <div class="ticks">
    <span><svg width="14" height="11"><path d="M1 6l4 4 8-9" fill="none" stroke="#fff" stroke-width="2"/></svg>Best Engineers &amp; Workers</span>
    <span><svg width="14" height="11"><path d="M1 6l4 4 8-9" fill="none" stroke="#fff" stroke-width="2"/></svg>On time Projects Completed</span>
    <span><svg width="14" height="11"><path d="M1 6l4 4 8-9" fill="none" stroke="#fff" stroke-width="2"/></svg>Factory in Worldwide</span>
    <span><svg width="14" height="11"><path d="M1 6l4 4 8-9" fill="none" stroke="#fff" stroke-width="2"/></svg>Sed ut perspiciatis unde omnis iste natus</span>
  </div>
  <div class="photo video" role="img" aria-label="Video still of plant valves and yellow pipework">
    <div class="play"><div class="ring"><svg width="34" height="34" viewBox="0 0 34 34"><circle cx="17" cy="17" r="15" fill="none" stroke="#fff" stroke-width="2"/><path d="M13 10l11 7-11 7z" fill="none" stroke="#fff" stroke-width="2"/></svg></div>WATCH VIDEO</div>
  </div>
  <div class="members-title">Members</div>
  <div class="member" style="top:106px"><div class="who"><i></i>Alden Marsh</div><p>Sed ut perspiciatis unde omnis iste nat us error sit voluptatem accusantium doloremque laudantium .</p><a>Read More</a></div>
  <div class="member" style="top:280px"><div class="who"><i></i>Curtis Marsh</div><p>Sed ut perspiciatis unde omnis iste nat us error sit voluptatem accusantium doloremque laudantium .</p><a>Read More</a></div>
  <div class="member" style="top:453px"><div class="who"><i></i>Dale Marsh</div><p>Sed ut perspiciatis unde omnis iste nat us error sit voluptatem accusantium doloremque laudantium .</p><a>Read More</a></div>
</section>

<section class="prospects">
  <h2 class="h2"><span class="mark"></span>Available Prospects</h2>
  <p class="lede">Sed ut perspiciatis unde omnis iste natus error sit voluptatem accusantium doloremque laudantium, totam rem aperiam, eaque ipsa quae ab illo inventore veritatis et quasi architecto beatae vitae dicta sunt explicabo.</p>
  <div class="card" style="left:81px"><div class="img" style="background:linear-gradient(180deg,#9fc3e6,#6f8fa8 70%,#4a4f55)" role="img" aria-label="Power plant chimneys against a blue sky"></div><div class="cap">POWER AND MACHINERY</div></div>
  <div class="card" style="left:446px"><div class="img" style="background:linear-gradient(180deg,#5e86b5,#7d8d9c 60%,#56606a)" role="img" aria-label="Oil field processing tanks and towers"></div><div class="cap">OIL FIELD SERVICES</div></div>
  <div class="card" style="left:809px"><div class="img" style="background:linear-gradient(180deg,#f2b24a,#c56a1f 55%,#3a2414)" role="img" aria-label="Industrial site with cranes at sunset"></div><div class="cap">MAINTENANCE REPAIR AND OVERHAUL</div></div>
</section>

<section class="contact">
  <h2 class="h2"><span class="mark"></span>Contact Us</h2>
  <p class="lede">Sed ut perspiciatis unde omnis iste natus error sit voluptatem accusantium doloremque laudantium, totam rem aperiam, eaque ipsa quae ab illo inventore veritatis et quasi architecto beatae vitae dicta sunt explicabo.</p>
  <div class="addr hi" style="left:81px"><h4><svg width="12" height="16" viewBox="0 0 12 16"><path d="M6 0a6 6 0 0 1 6 6c0 4-6 10-6 10S0 10 0 6a6 6 0 0 1 6-6z" fill="#fff"/><circle cx="6" cy="6" r="2" fill="#f07a1e"/></svg>ADDRESS</h4>Fort Worth Office<br>220 Harlow Street<br>Suite 310<br>Fort Worth, Texas 76102</div>
  <div class="addr" style="left:342px"><h4><svg width="12" height="16" viewBox="0 0 12 16"><path d="M6 0a6 6 0 0 1 6 6c0 4-6 10-6 10S0 10 0 6a6 6 0 0 1 6-6z" fill="#f07a1e"/><circle cx="6" cy="6" r="2" fill="#fff"/></svg>ADDRESS</h4>Oklahoma City Office<br>48 Cedar Lane<br>Suite 4<br>Oklahoma City, Oklahoma 73102<div class="ln">&#9743; 555.010.2405</div><div class="ln">&#9993; alden@ridgebackpetro.example</div></div>
  <div class="addr" style="left:606px"><h4><svg width="12" height="16" viewBox="0 0 12 16"><path d="M6 0a6 6 0 0 1 6 6c0 4-6 10-6 10S0 10 0 6a6 6 0 0 1 6-6z" fill="#f07a1e"/><circle cx="6" cy="6" r="2" fill="#fff"/></svg>ADDRESS</h4>Fort Worth Office<br>220 Harlow Street<br>Suite 310<br>Fort Worth, Texas 76102<div class="ln">&#9743; 555.010.2405</div><div class="ln">&#9993; alden@ridgebackpetro.example</div></div>
  <div class="addr" style="left:867px;width:254px"><h4><svg width="12" height="16" viewBox="0 0 12 16"><path d="M6 0a6 6 0 0 1 6 6c0 4-6 10-6 10S0 10 0 6a6 6 0 0 1 6-6z" fill="#f07a1e"/><circle cx="6" cy="6" r="2" fill="#fff"/></svg>ADDRESS</h4>Fort Worth Office<br>220 Harlow Street<br>Suite 310<br>Fort Worth, Texas 76102<div class="ln">&#9743; 555.010.7788</div><div class="ln">&#9993; curtis@ridgebackpetro.example</div></div>
</section>

<section class="enquiry">
  <h3>FOR ANY ENQUIRY</h3>
  <div class="field" style="left:81px;top:107px;width:250px">Name</div>
  <div class="field" style="left:342px;top:107px;width:250px">Last Name</div>
  <div class="field" style="left:81px;top:148px;width:250px">Email</div>
  <div class="field" style="left:342px;top:148px;width:250px">Phone No</div>
  <div class="field" style="left:602px;top:107px;width:250px;height:79px">Message</div>
  <span class="btn">SUBMIT</span>
</section>

<section class="clients">
  <h2 class="h2"><span class="mark"></span>Our Clients</h2>
  <p class="lede">Sed ut perspiciatis unde omnis iste natus error sit voluptatem accusantium doloremque laudantium, totam rem aperiam, eaque ipsa quae ab illo inventore veritatis et quasi architecto beatae vitae dicta sunt explicabo.</p>
  <div class="logos"><span>Corvane</span><span>Brightel</span><span>Netrunda</span><span>Swiftline</span><span>Global Assembly</span><span>Civitas</span><span>Maxwell Group</span></div>
</section>

<footer class="footer">
  <div class="brand"><span class="dot"></span><div><b>Ridgeback</b><small>Petroleum Ventures, LLC</small></div></div>
  <p class="about-txt">Sed ut perspiciatis unde omnis iste natus error sit voluptatem accusa ntium doloremque laudantium, totam rem aperiam, quae ab illodicta sunt explicabo.</p>
  <div class="social"><i></i><i></i><i></i><i></i></div>
  <div class="phone-btn">&#9743; 555.010.2400</div>
  <div class="col" style="left:451px"><h5>QUICK LINKS</h5><ul><li>Home</li><li>History</li><li>About Us</li><li>Available Prospects</li><li>Texas</li><li>Oklahoma</li><li>Contact Us</li></ul></div>
  <div class="col" style="left:641px"><h5>TESTIMONIALS</h5>
    <div class="quote"><b><span>&#8220;</span>Laura Pennick, Fairfax,</b>Nemo enim ipsam voluptatem quia voluptas sit aspernatur aut odit aut fugit, sed quia consequu sequi nesciunt</div>
    <div class="quote"><b><span>&#8220;</span>Laura Pennick, Fairfax,</b>Nemo enim ipsam voluptatem quia voluptas sit aspernatur aut odit aut fugit, sed quia consequu sequi nesciunt</div>
  </div>
  <div class="col" style="left:951px;width:170px"><h5>NEWS LETTER</h5><p style="font-size:12px;line-height:1.6">Nemo enim ipsam voluptatem quia voluptas sit aspernatur</p>
    <div class="news"><span>Enter Email</span><i><svg width="18" height="16" viewBox="0 0 18 16"><path d="M1 8L17 1l-4 14-4-5z" fill="none" stroke="#fff" stroke-width="1.6"/></svg></i></div></div>
</footer>
<section class="bottom">
  <span style="left:81px">&copy; Copyright 2017. All rights reserved</span>
  <span style="right:81px">Privacy Policies</span>
</section>
</body>
</html>
```